i need a business card for a plumbing company in california

we are a drain cleaning , maintenance plumbing company who is starting new marketing campaign for a tatrench-less pipe installation department .

Target Market(s)

the professional who appreciates time and quality workmanship.

Industry/Entity Type

Plumbing

Colors
0655a3
ec1f27

Requirements
Must have
• the second logo needs to be included
Nice to have
• a focus on the services offered
Should not have
• any underlined words on the brief

```html
<!DOCTYPE html>
<html lang="en">
<head>
<meta charset="utf-8">
<title>Business Card</title>
<link href="https://fonts.googleapis.com/css2?family=Arimo:wght@400;700&display=swap" rel="stylesheet">
<style>
  :root {
    --page-bg: #d9d3cb;
    --card-top: #f4f3f1;
    --card-top-end: #dcdad7;
    --ink-grey: #555250;
    --band-grey: #3d3b39;
    --band-text: #e4e2df;
    --brand-red: #ec1f27;
    --brand-red-deep: #a3161c;
    --brand-blue: #0655a3;
    --contact-text: #f6dcdc;
  }
  * { margin: 0; padding: 0; box-sizing: border-box; }
  html, body {
    width: 1200px; height: 970px; overflow: hidden;
    background: var(--page-bg);
    font-family: "Arimo", Arial, sans-serif;
  }
  .business-card {
    position: absolute; left: 100px; top: 199px;
    width: 1000px; height: 572px;
    background: linear-gradient(160deg, var(--card-top) 0%, var(--card-top-end) 100%);
    overflow: hidden;
    box-shadow: 0 10px 30px rgba(0,0,0,.18);
  }
  .brand {
    position: absolute; left: 55px; top: 92px;
    display: flex; align-items: flex-end; gap: 22px;
  }
  .brand-name {
    font-weight: 700; font-size: 62px; line-height: 64px;
    color: var(--ink-grey); letter-spacing: -1px;
  }
  .brand-mark {
    width: 36px; height: 36px; background: var(--brand-red);
    margin-bottom: 12px;
  }
  .title-band {
    position: absolute; left: 0; top: 296px; width: 760px; height: 54px;
    background: var(--band-grey);
    clip-path: polygon(0 0, 740px 0, 760px 22px, 760px 54px, 0 54px);
    display: flex; align-items: center; padding-left: 55px;
    color: var(--band-text);
  }
  .person-name { font-weight: 700; font-size: 31px; }
  .divider { width: 2px; height: 32px; background: var(--band-text); margin: 0 26px; opacity: .8; }
  .person-role { font-size: 25px; }
  .contact-panel {
    position: absolute; left: 0; top: 352px; width: 1000px; height: 220px;
    background: linear-gradient(90deg, var(--brand-red-deep) 0%, #c8202a 45%, #b81c24 75%, rgba(200,32,42,.55) 100%);
  }
  .address {
    position: absolute; left: 55px; top: 18px;
    font-size: 24px; line-height: 32px; color: var(--contact-text);
  }
  .contact-list {
    position: absolute; left: 55px; top: 90px; list-style: none;
    font-size: 24px; color: var(--contact-text);
  }
  .contact-list li { display: flex; align-items: center; height: 36px; }
  .contact-list svg { width: 28px; height: 28px; margin-right: 10px; flex: none; }
  .icon-disc { fill: var(--brand-blue); stroke: #f6dcdc; stroke-width: 1.5; }
</style>
</head>
<body>
  <section class="business-card">
    <div class="brand">
      <div class="brand-name">Keystone<br>Pipeworks</div>
      <div class="brand-mark"></div>
    </div>

    <div class="title-band">
      <span class="person-name">Dale Moreno</span>
      <span class="divider"></span>
      <span class="person-role">President</span>
    </div>

    <div class="contact-panel">
      <p class="address">PO Box 418, 2210 Harbor Blvd<br>Costa Mesa, CA 92626</p>
      <ul class="contact-list">
        <li>
          <svg viewBox="0 0 28 28" aria-hidden="true"><circle class="icon-disc" cx="14" cy="14" r="12"/><path d="M8 11 Q14 6 20 11 L18 13 L16 11 L12 11 L10 13 Z M10 14 H18 V19 H10 Z" fill="#f6dcdc"/></svg>
          (714) 555-0182
        </li>
        <li>
          <svg viewBox="0 0 28 28" aria-hidden="true"><circle class="icon-disc" cx="14" cy="14" r="12"/><rect x="8" y="10" width="12" height="9" fill="none" stroke="#f6dcdc" stroke-width="1.6"/><path d="M8 10 L14 15 L20 10" fill="none" stroke="#f6dcdc" stroke-width="1.6"/></svg>
          info@keystonepipeworks.com
        </li>
        <li>
          <svg viewBox="0 0 28 28" aria-hidden="true"><circle class="icon-disc" cx="14" cy="14" r="12"/><circle cx="14" cy="14" r="7" fill="none" stroke="#f6dcdc" stroke-width="1.4"/><ellipse cx="14" cy="14" rx="3" ry="7" fill="none" stroke="#f6dcdc" stroke-width="1.2"/><path d="M7 14 H21" stroke="#f6dcdc" stroke-width="1.2"/></svg>
          www.keystonepipeworks.com
        </li>
      </ul>
    </div>
  </section>
</body>
</html>
```